Halvard Atelier Business cards

Design our business cards and eventually a logo. The company is based in Paris, its activity is the retailing via internet of luxury home furniture (like Vambrelli, Bercusa, tarvoni...) Our clients are international andwith a high sense of aesthetics. The design shall communicate wealth and trust with a high quality and aesthetic sense, pure lines Company Name is Halvard AtelierExplanation of the name: usually people who wants to buy furniture usually go in a showroom. Today they go in showroom to test the furniture and they search for the price on internet, which is a "Halvard atelier".We will not be a e-commerce site. Our site will be (another project) a presentation site which purpose is to reach qualified prospects. Then everything will be handled by phone, meeting etc.The business card must be professional as we will negotiate with many luxury brands, opportunity to represent them on our site, prices etc.As far as the color are concerned mostly black and whithe or grey. The font of the Halvard Atelier name shall have some impact.

Target Market(s)

High-end furniture and buyers of luxury goods, international customers, mostly women who handle such projects.
We also deal with professional buyers (hotels as an example) and luxury brands

Contact Information for Business Card

standard format 85x55, lanscape card, square corners will be printed on thick high quality paper (300 or 350g)

Font styles to use
Sans Serif

Colors

Designer to choose colors to be used in the design.

Requirements
Must have
• Must be white, as the paper will be high quality, the paper will enhance the card.
• Name of the brand Halvard atelier (with specific font which make it very nice looking and catch the attention. similar to Calibri or Calibri
• Name of person (will give you the name later (4 names and position)
• the position of the person
• +33 6 41 27 58 93, claire.vasseur@halvardatelier.fr, Physical address 27, rue Fenouillard, 75005 Paris, France (courrier only) our web site www.halvardatelier.fr
• The card must be simple and class
Nice to have
• Font of the address is smaller than the rest,
• Calibri font or similar on recto side with the name of the company which may look similar to the picture inserted in the brief.
• The grey color in the picture inserted is ok for us
Should not have
• Any parallel lines which represent the name of the company
• Any heavy design If you go on internet sites which present the furniture all designs are pure lines and high quality craftsmanship. To have an idea of our targetted client or brand we will be in touch: https://www.casavelumi.it/projects/
• Note that the picture added below is what we use, now as mail signature, up to you to have a better design etc.

```html
<!DOCTYPE html>
<html lang="fr">
<head>
<meta charset="utf-8">
<title>Halvard Atelier – Business card</title>
<link rel="stylesheet" href="https://fonts.googleapis.com/css2?family=Carlito:wght@400;700&display=swap">
<style>
  :root {
    --charcoal: #2e2d2e;
    --charcoal-soft: #3a393a;
    --mist: #f1f0ef;
    --rule: #b9b7b5;
    --paper: #ffffff;
    --text: #1e1e1e;
    --text-muted: #6b6a69;
  }
  html, body {
    margin: 0;
    padding: 0;
    overflow: hidden;
    background: var(--paper);
  }
  .card {
    position: relative;
    width: 1200px;
    height: 686px;
    overflow: hidden;
    background: var(--paper);
    font-family: "Carlito", "Calibri", Arial, sans-serif;
    color: var(--text);
  }
  .card__shapes {
    position: absolute;
    inset: 0;
    width: 1200px;
    height: 686px;
  }
  .brand {
    position: absolute;
    left: 78px;
    top: 58px;
    margin: 0;
    font-weight: 700;
    font-size: 72px;
    line-height: 1;
    letter-spacing: 6px;
    text-transform: uppercase;
    color: var(--paper);
  }
  .brand__line {
    display: block;
  }
  .brand__line--second {
    padding-left: 96px;
    margin-top: 8px;
  }
  .contact {
    position: absolute;
    left: 78px;
    top: 326px;
    margin: 0;
  }
  .contact__name {
    margin: 0;
    font-weight: 700;
    font-size: 40px;
    line-height: 1.1;
    letter-spacing: 1px;
  }
  .contact__role {
    margin: 4px 0 0;
    font-size: 24px;
    line-height: 1.2;
    letter-spacing: 2px;
    text-transform: uppercase;
    color: var(--text-muted);
  }
  .contact__details {
    margin: 22px 0 0;
    padding: 0;
    list-style: none;
    font-size: 26px;
    line-height: 1.4;
  }
  .contact__address {
    margin: 8px 0 0;
    font-size: 21px;
    line-height: 1.3;
    color: var(--text-muted);
  }
  .website {
    position: absolute;
    left: 700px;
    top: 612px;
    margin: 0;
    display: flex;
    align-items: center;
    gap: 14px;
    font-size: 32px;
    line-height: 1;
    color: var(--text);
  }
  .website__icon {
    width: 32px;
    height: 32px;
    flex: none;
  }
</style>
</head>
<body>
  <main class="card">
    <svg class="card__shapes" viewBox="0 0 1200 686" aria-hidden="true">
      <rect class="mist-field" x="0" y="0" width="1200" height="686" fill="var(--mist)"/>
      <path class="charcoal-field"
            d="M0 0 H890 L708 232 Q672 292 612 292 H0 Z"
            fill="var(--charcoal)"/>
      <path class="paper-band"
            d="M1200 538 H735 Q690 538 672 568 Q656 598 610 598 H0 V686 H1200 Z"
            fill="var(--paper)"/>
      <line class="contact-rule" x1="78" y1="312" x2="78" y2="312" stroke="var(--rule)"/>
    </svg>

    <h1 class="brand">
      <span class="brand__line">Halvard</span>
      <span class="brand__line brand__line--second">Atelier</span>
    </h1>

    <section class="contact">
      <p class="contact__name">Claire Vasseur</p>
      <p class="contact__role">Directrice commerciale</p>
      <ul class="contact__details">
        <li>+33 6 41 27 58 93</li>
        <li>claire.vasseur@halvardatelier.fr</li>
      </ul>
      <p class="contact__address">27, rue Fenouillard, 75005 Paris, France</p>
    </section>

    <p class="website">
      <svg class="website__icon" viewBox="0 0 34 34" aria-hidden="true">
        <circle cx="17" cy="17" r="15" fill="var(--text)"/>
        <g fill="none" stroke="var(--paper)" stroke-width="1.6">
          <ellipse cx="17" cy="17" rx="6.5" ry="14.5"/>
          <line x1="17" y1="2.5" x2="17" y2="31.5"/>
          <line x1="2.5" y1="17" x2="31.5" y2="17"/>
          <path d="M5 9.5 Q17 13 29 9.5"/>
          <path d="M5 24.5 Q17 21 29 24.5"/>
        </g>
      </svg>
      <span class="website__url">www.halvardatelier.fr</span>
    </p>
  </main>
</body>
</html>
```